Flyer Design Project

Hi, I need a flyer designed for my Personal Training Studio. I have been doing early morning and afternoon appointments but am now able to offer appointments during the day. My Studio is situated on my property which is about 15mins drive from Orange at a small rural suburb called Borenore. My training sessions are completely private and I specialise on training individuals or two people. I already have a logo and a face book page under my trading name which is Elevate Me Personal Training. I want the flyer for a letter box drop around my area to target new clients that would find my location convenient and the setting appealing.
Updates
Logo file is now attached.
Target Market(s)
Local people close to my area
Industry/Entity Type
Training
Requirements
Must have
- Logo (attached)

```html
<!DOCTYPE html>
<html lang="en">
<head>
<meta charset="utf-8">
<title>Elevate Me Personal Training – Flyer</title>
<link rel="stylesheet" href="https://fonts.googleapis.com/css2?family=Kalam:wght@400;700&family=Oswald:wght@300;400&family=Varela+Round&display=swap">
<style>
  :root {
    --lime: #8df72b;
    --brand-blue: #1f5fd6;
    --teal-light: #4fd8d5;
    --teal-dark: #1f9a86;
    --ink: #111111;
    --white: #ffffff;
    --photo-sky: #6fa3c9;
    --photo-grass: #3f7a3a;
    --photo-skin: #c89a7c;
  }
  * { box-sizing: border-box; margin: 0; padding: 0; }
  html, body { width: 849px; height: 1200px; overflow: hidden; background: var(--white); }
  .flyer { position: relative; width: 849px; height: 1200px; overflow: hidden; background: var(--white); }

  /* Brand header */
  .brand { position: absolute; left: 52px; top: 40px; display: flex; align-items: center; gap: 50px; }
  .brand-dot { width: 208px; height: 208px; border-radius: 50%; background: var(--brand-blue); flex: none; }
  .brand-name { font-family: "Varela Round", sans-serif; font-weight: 400; color: var(--brand-blue); line-height: 1; white-space: nowrap; }
  .brand-name .line-1 { display: block; font-size: 82px; }
  .brand-name .line-2 { display: block; font-size: 52px; margin-top: 10px; }

  /* Left lime column */
  .lime-panel { position: absolute; left: 0; top: 0; width: 369px; height: 1200px; }
  .tagline { position: absolute; font-family: "Oswald", sans-serif; font-weight: 300; color: var(--white); line-height: 1; white-space: nowrap; }
  .tagline.first { left: 51px; top: 385px; font-size: 42px; }
  .tagline.second { left: 140px; top: 425px; font-size: 50px; }
  .swoosh { position: absolute; left: 30px; top: 480px; width: 290px; height: 50px; }

  .goal-heading { position: absolute; left: 29px; top: 558px; font-family: "Oswald", sans-serif; font-weight: 300; font-size: 30px; color: var(--ink); white-space: nowrap; }
  .goal-copy { position: absolute; left: 38px; top: 608px; font-family: "Kalam", cursive; font-size: 19px; letter-spacing: 1px; line-height: 24.2px; color: var(--ink); white-space: nowrap; }

  .gallery { position: absolute; left: 44px; top: 964px; width: 290px; height: 144px; display: flex; }
  .gallery .shot { flex: 1; height: 100%; }
  .shot.lake { background: linear-gradient(180deg, #7d9fa8, #a0705f); }
  .shot.studio { background: linear-gradient(180deg, #f2f2f2, #cfa891); }
  .shot.stone { background: linear-gradient(180deg, #b9b3a5, #c2946f); }
  .shot.stage { background: linear-gradient(180deg, #3b2a22, #a9573c); }

  .shape-call { position: absolute; left: 16px; top: 1112px; font-family: "Varela Round", sans-serif; font-size: 48px; color: #eaf6ff; -webkit-text-stroke: 1px #2a6fd0; white-space: nowrap; }

  /* Right column */
  .hero-band { position: absolute; left: 369px; top: 267px; width: 480px; height: 433px; background: linear-gradient(90deg, var(--teal-light), var(--teal-dark)); }
  .hero-photo { position: absolute; left: 83px; top: 3px; width: 280px; height: 413px; border-radius: 50%; background: linear-gradient(180deg, var(--photo-sky) 0%, var(--photo-grass) 45%, var(--photo-skin) 60%, #2c3136 80%, #4c8c3c 100%); }

  .course-info { position: absolute; left: 392px; top: 716px; font-family: "Kalam", cursive; color: var(--ink); white-space: nowrap; }
  .course-info h2 { font-size: 24px; font-weight: 400; letter-spacing: 1px; line-height: 30px; }
  .course-info p { font-size: 19px; letter-spacing: 1px; line-height: 24.2px; margin-bottom: 4px; }

  .contact-band { position: absolute; left: 369px; top: 1038px; width: 480px; height: 162px; background: linear-gradient(90deg, var(--teal-light), var(--teal-dark)); }
  .contact-list { list-style: none; position: absolute; left: 27px; top: 14px; font-family: "Oswald", sans-serif; font-weight: 300; font-size: 23px; line-height: 34px; color: var(--white); white-space: nowrap; }
</style>
</head>
<body>
<main class="flyer">
  <svg class="lime-panel" viewBox="0 0 369 1200" aria-hidden="true">
    <path d="M0 270 Q170 385 369 262 L369 1200 L0 1200 Z" fill="var(--lime)"/>
  </svg>

  <header class="brand">
    <div class="brand-dot" aria-hidden="true"></div>
    <h1 class="brand-name"><span class="line-1">Elevate Me</span><span class="line-2">Personal Training</span></h1>
  </header>

  <p class="tagline first">look good and</p>
  <p class="tagline second">feel good</p>
  <svg class="swoosh" viewBox="0 0 290 50" aria-hidden="true">
    <defs>
      <linearGradient id="swooshFill" x1="0" x2="1">
        <stop offset="0" stop-color="#7fd3e0"/>
        <stop offset="1" stop-color="#1f7fc8"/>
      </linearGradient>
    </defs>
    <path d="M2 40 Q160 48 288 4 Q200 44 2 42 Z" fill="url(#swooshFill)"/>
  </svg>

  <h2 class="goal-heading">Goal of my personal training</h2>
  <p class="goal-copy">&nbsp;&nbsp;Lorem ipsum dolor sit<br>amet, consectetuer adipiscing<br>elit, sed diam nonummy nibh<br>euismod tincidunt ut laoreet<br>dolore magna aliquam erat<br>volutpat. Ut wisi enim ad<br>minim veniam, quis nostrud<br>exerci tation ullamcorper<br>suscipit lobortis nisl ut aliquip<br>ex ea commodo Duis autem vel<br>eum iriure dolor in hendrerit in<br>vulputate velit esse molestie<br>consequat, vel illum dolore</p>

  <div class="gallery">
    <div class="shot lake" role="img" aria-label="Photo of the trainer in sportswear by a lake"></div>
    <div class="shot studio" role="img" aria-label="Studio photo of the trainer in a sports top"></div>
    <div class="shot stone" role="img" aria-label="Photo of the trainer against a stone wall"></div>
    <div class="shot stage" role="img" aria-label="Photo of the trainer at a fitness competition"></div>
  </div>
  <p class="shape-call">Get into Shape</p>

  <section class="hero-band">
    <div class="hero-photo" role="img" aria-label="Photo of a woman sprinting on an outdoor track"></div>
  </section>

  <section class="course-info">
    <h2>Courses:</h2>
    <p>accumsan et iusto odio dignissim qui blandit<br>praesent luptatum zzril delenit augue duis<br>dolore te feugait nulla facilisi. Nam liber<br>tempor cum soluta nobis eleifend option</p>
    <h2>Course topics:</h2>
    <p>doming id quod mazim placerat facer possim<br>assum. Typi non habent claritatem insitam;<br>est usus legentis in iis qui facit eorum<br>claritatem. Investigationes demonstraverunt<br>lectores legere me lius quod ii legunt</p>
  </section>

  <footer class="contact-band">
    <ul class="contact-list">
      <li>Call for free consultation: 73900012458</li>
      <li>Time:</li>
      <li>Website:</li>
      <li>Catch me on Friendloop:</li>
    </ul>
  </footer>
</main>
</body>
</html>
```